Sales presentation introduction for Finance and Tech firms

Our business is two fold - 1) recruitment 2) consultancy. We would like a one or two page template that we can use to send to potential clients. The template will ideally be the same for the recruitment and consultancy side. We need to be able to edit the template to enter text.

I have attached our logo so you can see what we currently use on Brindlepost.

Sector is financial services and technology. We do not intent to have lots of text but the layout/images/designs to be used should cover some of page in a way that it takes up some space to avoid having to write lot of text.

Open to colour suggestions.

Please look at the attached word doc to see the text I would like for the two presentations.

Happy to answer questions.

Target Market(s)

Directors

Industry/Entity Type

Finance and tech companies

Colors
0094D4
00A9DD
6FCCEA
C7EBF8
E9F6FB

Requirements
Must have
• Editable text

```html
<!DOCTYPE html>
<html lang="en">
<head>
<meta charset="utf-8">
<title>Corvanta – Recruitment &amp; Consultancy Flyers</title>
<link href="https://fonts.googleapis.com/css2?family=Montserrat:wght@500;700&family=Roboto+Condensed:wght@400&family=Roboto:wght@300;400;500&display=swap" rel="stylesheet">
<style>
:root{
  --backdrop:#0d4a85;
  --navy:#1b3566;
  --royal:#1d5aa8;
  --bright:#0094d4;
  --sky:#6fcaee;
  --ice:#c7ebf8;
  --paper:#ffffff;
  --ink:#1c1c1c;
  --grey:#6b6e73;
}
*{margin:0;padding:0;box-sizing:border-box}
html,body{width:1200px;height:644px;overflow:hidden}
body{background:var(--backdrop);position:relative;font-family:"Roboto",Arial,sans-serif;color:var(--ink)}
.page{position:absolute;top:40px;width:428px;height:555px;background:var(--paper);box-shadow:0 6px 14px rgba(0,0,0,.35);overflow:hidden}
.page--recruitment{left:61px}
.page--consultancy{left:679px}
.header-art{position:absolute;left:0;top:0;width:428px;height:222px}
.brand{position:absolute;left:30px;top:66px;display:flex;align-items:center;gap:7px}
.brand-mark{width:14px;height:14px;background:var(--royal)}
.brand-name{font-family:"Roboto",Arial,sans-serif;font-weight:400;font-size:21px;color:var(--grey);letter-spacing:.5px}
.band-title{position:absolute;font-family:"Roboto Condensed",Arial,sans-serif;color:#fff;text-transform:uppercase;line-height:1;white-space:nowrap}
.band-left .band-title{font-size:12.5px}
.band-note{position:absolute;font-family:"Roboto Condensed",Arial,sans-serif;color:#fff;font-size:7px;line-height:9.4px;white-space:nowrap}
.band-left{position:absolute;left:23px;top:158px;width:195px}
.band-left .band-note{top:17px;left:0}
.band-right{position:absolute;left:270px;top:154px;width:155px}
.band-right .band-title{font-size:17px}
.band-right .band-note{top:22px;left:10px;text-transform:uppercase;text-align:center}
.consult-title{font-size:16.5px}
.page--consultancy .band-left .band-title{font-size:16px}
.page--consultancy .band-left .band-note{top:22px}
.intro-head{position:absolute;left:24px;top:231px;font-family:"Montserrat",Arial,sans-serif;font-weight:700;font-size:14px;line-height:18.5px;color:var(--ink)}
.intro-rule{position:absolute;left:182px;top:232px;width:1px;height:34px;background:var(--bright)}
.intro-copy{position:absolute;left:201px;top:233px;width:210px;font-size:8px;line-height:12.6px}
.body-copy{position:absolute;font-size:8px;line-height:12.6px;text-align:justify}
.body-copy--set{white-space:nowrap;text-align:left}
.section-head{position:absolute;font-family:"Roboto",Arial,sans-serif;font-weight:400;font-size:15px;color:var(--ink)}
.team-photo{position:absolute;left:25px;top:284px;width:160px;height:129px;border:7px solid var(--royal);background:linear-gradient(135deg,#e9eef4,#b9c4d2 60%,#3d4a63)}
.tagline{position:absolute;left:24px;top:497px;font-family:"Montserrat",Arial,sans-serif;font-weight:700;font-size:10.5px}
.footer{position:absolute;left:0;top:515px;width:428px;height:28px}
.footer-address{position:absolute;left:24px;top:522px;font-family:"Montserrat",Arial,sans-serif;font-weight:500;font-size:9.6px;color:#fff}
.footer-web{position:absolute;left:306px;top:519px;font-family:"Montserrat",Arial,sans-serif;font-size:6.4px;line-height:8px;color:#fff}
.work-head{position:absolute;left:25px;top:280px;font-weight:300;font-size:24px;color:var(--royal)}
.checklist{position:absolute;left:25px;top:318px;list-style:none}
.checklist li{display:flex;align-items:center;gap:6px;font-size:10.5px;height:20px}
.checklist svg{width:10px;height:10px}
.advisor-photo{position:absolute;left:214px;top:283px;width:202px;height:202px;background:radial-gradient(circle at 65% 40%,#f1f1f1,#d9dde2 55%,#ffffff 80%)}
.phone-band{position:absolute;left:258px;top:484px;width:170px;height:32px}
.phone-number{position:absolute;left:305px;top:487px;font-family:"Roboto",Arial,sans-serif;font-weight:500;font-size:18px;color:#fff}
.phone-icon{position:absolute;left:286px;top:492px;width:14px;height:14px}
</style>
</head>
<body>

<section class="page page--recruitment">
  <svg class="header-art" viewBox="0 0 428 222">
    <rect width="428" height="222" fill="#fff"/>
    <polygon points="144,0 428,0 428,148 228,148" fill="#c7a98e" role="img" aria-label="Photo of candidates seated in a waiting area"/>
    <polygon points="144,0 428,0 428,80 190,60" fill="#8aa0bd" opacity=".55"/>
    <polygon points="110,145 185,88 215,145" fill="var(--sky)"/>
    <polygon points="150,145 212,110 232,145" fill="var(--bright)"/>
    <polygon points="134,0 148,0 272,210 258,210" fill="var(--royal)"/>
    <polygon points="0,145 214,145 236,202 0,202" fill="var(--navy)"/>
    <polygon points="248,145 428,145 428,202 272,202" fill="var(--royal)"/>
    <rect y="209" width="428" height="9" fill="var(--sky)"/>
  </svg>
  <div class="brand"><span class="brand-mark"></span><span class="brand-name">CORVANTA</span></div>
  <div class="band-left">
    <div class="band-title">Target the right candidates</div>
    <p class="band-note">Trying to find an employee that will not only fit with the job you<br>are hiring for but also your company culture can be a challenge.</p>
  </div>
  <div class="band-right">
    <div class="band-title">We are hiring</div>
    <p class="band-note">Are you a graduate or undergraduate<br>with prior BPO experience?</p>
  </div>

  <h2 class="intro-head">We Help Business<br>Grow Effeciently</h2>
  <span class="intro-rule"></span>
  <p class="intro-copy">Job seekers use social media to research companies and learn about new job opportunities. Use this example of 'We're hiring' social media post to create</p>

  <div class="team-photo" role="img" aria-label="Photo of three colleagues reviewing documents at a desk"></div>
  <h3 class="section-head" style="left:203px;top:283px">Job seekers</h3>
  <p class="body-copy" style="left:201px;top:304px;width:207px">Job seekers use social media to research companies and learn about new job opportunities. Use this example of 'We're hiring' social media post to create Job seekers use social media to research companies and learn about new job opportunities.</p>
  <p class="body-copy" style="left:201px;top:380px;width:207px">Use this example of 'We're hiring' social media post to create Job seekers use social media to research compa&shy;nies and learn about new job opportunities.</p>
  <h3 class="section-head" style="left:26px;top:425px">Job seekers</h3>
  <p class="body-copy" style="left:26px;top:449px;width:382px">Job seekers use social media to research companies and learn about new job opportunities. Use this example of 'We're hiring' social media post to create Job seekers use social media to research companies and learn about new job opportunities.</p>

  <p class="tagline">We Help Business Grow Effeciently</p>
  <svg class="footer" viewBox="0 0 428 28">
    <polygon points="0,0 232,0 244,28 0,28" fill="var(--navy)"/>
    <polygon points="236,0 256,0 268,28 248,28" fill="#c9cfe8"/>
    <polygon points="254,0 270,0 282,28 266,28" fill="#8e9bd0"/>
    <polygon points="264,0 428,0 428,28 280,28" fill="var(--royal)"/>
  </svg>
  <p class="footer-address">48 Harrowgate Street Fairview, NY 10452</p>
  <p class="footer-web">hello@corvanta-mail.com<br>www.corvanta-mail.com</p>
</section>

<section class="page page--consultancy">
  <svg class="header-art" viewBox="0 0 428 222">
    <rect width="428" height="222" fill="#fff"/>
    <polygon points="144,0 428,0 428,148 228,148" fill="#5c86b8" role="img" aria-label="Photo of hands using a tablet with glowing financial data"/>
    <polygon points="170,0 330,0 300,148 228,148" fill="#b9d9ee" opacity=".6"/>
    <polygon points="110,145 185,88 215,145" fill="var(--sky)"/>
    <polygon points="150,145 212,110 232,145" fill="var(--bright)"/>
    <polygon points="134,0 148,0 272,210 258,210" fill="var(--royal)"/>
    <polygon points="0,145 214,145 236,202 0,202" fill="var(--navy)"/>
    <polygon points="248,145 428,145 428,202 272,202" fill="var(--royal)"/>
    <rect y="209" width="428" height="9" fill="var(--sky)"/>
  </svg>
  <div class="brand"><span class="brand-mark"></span><span class="brand-name">CORVANTA</span></div>
  <div class="band-left">
    <div class="band-title">Finance and tech firms</div>
    <p class="band-note">Trying to find an employee that will not only fit with the job you<br>are hiring for but also your company culture can be a challenge.</p>
  </div>
  <div class="band-right">
    <div class="band-title consult-title">Consultancy</div>
    <p class="band-note">Are you a graduate or undergraduate<br>with prior BPO experience?</p>
  </div>

  <h2 class="intro-head">We Help Business<br>Grow Effeciently</h2>
  <span class="intro-rule"></span>
  <p class="intro-copy">Job seekers use social media to research companies and learn about new job opportunities. Use this example of 'We're hiring' social media post to create</p>

  <div class="advisor-photo" role="img" aria-label="Photo of a consultant presenting a growth chart on a tablet"></div>
  <h3 class="work-head">Work you'll do</h3>
  <ul class="checklist">
    <li><svg viewBox="0 0 10 10"><path d="M1 5.5 L4 8.5 L9 1.5" fill="none" stroke="var(--royal)" stroke-width="2"/></svg>Drive end-to-end transformation.</li>
    <li><svg viewBox="0 0 10 10"><path d="M1 5.5 L4 8.5 L9 1.5" fill="none" stroke="var(--royal)" stroke-width="2"/></svg>Lead epic disruption.</li>
    <li><svg viewBox="0 0 10 10"><path d="M1 5.5 L4 8.5 L9 1.5" fill="none" stroke="var(--royal)" stroke-width="2"/></svg>Partner with the biggest clients.</li>
  </ul>
  <p class="body-copy body-copy--set" style="left:27px;top:383px">Job seekers use social media to research compa-<br>nies and learn about new job opportunities. Use this<br>example of 'We're hiring' social media post to create</p>
  <h3 class="section-head" style="left:26px;top:425px">Job seekers</h3>
  <p class="body-copy body-copy--set" style="left:27px;top:449px">Job seekers use social media to research companies and learn about<br>new job opportunities. Use this example of 'We're hiring' social media<br>post to create</p>

  <svg class="phone-band" viewBox="0 0 170 32"><polygon points="0,0 170,0 170,32 14,32" fill="var(--navy)"/></svg>
  <svg class="phone-icon" viewBox="0 0 24 24"><path d="M6.6 2.5 9.5 6.5 7.6 8.9c1.3 2.9 4.1 5.8 7.5 7.5l2.4-1.9 4 2.9-1.6 3.6c-8.2.4-17.3-8.6-16.9-16.9z" fill="none" stroke="#fff" stroke-width="1.6" stroke-linejoin="round"/></svg>
  <p class="phone-number">5550192847</p>

  <p class="tagline">We Help Business Grow Effeciently</p>
  <svg class="footer" viewBox="0 0 428 28">
    <polygon points="0,0 232,0 244,28 0,28" fill="var(--navy)"/>
    <polygon points="236,0 256,0 268,28 248,28" fill="#c9cfe8"/>
    <polygon points="254,0 270,0 282,28 266,28" fill="#8e9bd0"/>
    <polygon points="264,0 428,0 428,28 280,28" fill="var(--royal)"/>
  </svg>
  <p class="footer-address">48 Harrowgate Street Fairview, NY 10452</p>
  <p class="footer-web">hello@corvanta-mail.com<br>www.corvanta-mail.com</p>
</section>

</body>
</html>
```